Swimming Pool Service Website needed!!!

Hi Everyone! Thanks for looking at my contest. I PROMISE to provide excellent feedback during this process.

I am starting a new swimming pool business cleaning company in San Diego, California and would like your help in making it similar to one of these two websites that are already functioning.

http://www.brightlagoonworks.example/services-repair.html

http://tidemarkaquacare.example/commercial-pool-cleaning.php

I like these two because they are easy to read, classy, sophisticated and have nice pictures of really clean & clear pools.

I really like the blue on white color format.

I do not have a logo, but the name of my company is GLIMMERWAVE POOL SERVICE.

My tag line is: Water so pure, it sparkles like a summer sky. (does not need to have the quotes around "in"...maybe just italics for this word IN?) You decide for me.

I would like to have a logo designed that incorporates some sort of easy to read letters. I do not want cursive (handwriting) letters. I thought about having a "reflection" of letters (mirror image), but think that this will be hard to read from far away. Maybe you can surprise me and come up with an idea that works using the a mirror image....but I'm not sure. I was leaning toward plain old BLOCK letters as I think it would be easy to read on my truck.

I would like to have 5 pages on my website:
1) Home
2) About Us (Know Your Poolman) / Why Hire Us
3) Services Offered
4) FAQ's
5) Contact

I am looking for a fully-functioning website (coded). Upon selection of the design winner, I am offering to increase the budget/payment by $100-$125 for the coding of all the pages. So anyone looking at participating in this contest, should be willing and able to provide the coding to the webpages that i've requested.

Target Market(s)

Upper middle-class homeowners who have a pool

Industry/Entity Type

Pool Service

Number of Pages Required

5+ page

Font styles to use
Serif

Colors
0455a3
3276b5
85acd3
85cae6
ffffff
33a6d7
0592cd

Requirements
Must have
• The Home page must have this picture highlighted in the top of the page:
• http://www.mesawaterpro.example/
• Must have pictures of some high-end pools. Any that you can find on the internet are wonderful.
• Must have a table on the right of the home page that mentions the service areas that we go to:
• • Carmel Valley (92130)
• • Del Mar (92014)
• • Rancho Santa Fe (92067)
• • Solana Beach (92075)
• • Santaluz (92127)
• • Cardiff (92007)
• • Encinitas (92024)
• • Carlsbad (92009, 92008)
• • La Jolla (92037)
• • Pacific Beach (92109)
• • Mira Mesa (92126)
• • Sorrento Valley (92121)
• • Clairemont (92117)
• • Rancho Bernardo (92127, 92128)
• • Rancho Penasquitos (92129)
• • Poway (92064)
• •
Nice to have
• Maybe incorporate some pictures of some kids (or families) playing in pools on the Why Hire Us page?
• I also like the feel of this website, but posting this page just for reference so you can get a feel more of what I like:
• http://www.crestlinepool.example/
• I like the FAQ's page from this website. I like how you can click on the question and then it pops up with the answer. http://www.dunewoodpoolcare.example/pool-spa-fountain-faqs/

```html
<!DOCTYPE html>
<html lang="en">
<head>
<meta charset="utf-8">
<title>Glimmerwave Pool Service</title>
<link rel="stylesheet" href="https://fonts.googleapis.com/css2?family=Raleway:ital,wght@0,400;0,500;0,600;1,400&family=Open+Sans:ital,wght@0,400;0,600;1,400&display=swap">
<style>
:root{
  --navy:#0455a3;
  --blue:#3276b5;
  --sky:#85acd3;
  --aqua:#85cae6;
  --cyan:#33a6d7;
  --ocean:#0592cd;
  --white:#ffffff;
  --ink:#1f1f1f;
  --text:#3a3a3a;
  --muted:#6a6a6a;
  --line:#d6d6d6;
}
*{margin:0;padding:0;box-sizing:border-box}
html,body{width:1106px;height:1200px;overflow:hidden;background:var(--white)}
body{position:relative;font-family:'Open Sans',sans-serif;color:var(--text)}
.abs{position:absolute}

/* header */
.brand{left:162px;top:30px;display:flex;align-items:center;gap:8px}
.brand-dot{width:26px;height:26px;border-radius:50%;background:var(--navy)}
.brand-name{font-family:'Raleway',sans-serif;font-weight:500;font-size:25px;color:var(--navy);letter-spacing:.2px}
.contact{right:176px;top:36px;text-align:right}
.contact-phone{font-family:'Raleway',sans-serif;font-size:18px;color:#555;display:flex;align-items:center;justify-content:flex-end;gap:5px}
.contact-mail{font-size:11px;color:#555;margin-top:4px;display:flex;align-items:center;justify-content:flex-end;gap:5px}

/* nav */
.nav{left:167px;top:89px;width:772px;height:49px;border-radius:3px 3px 0 0;
  background:linear-gradient(#5ab6e6,#1a8fd2 55%,#1383c8);display:flex}
.nav a{font-family:'Raleway',sans-serif;font-size:14.5px;color:var(--white);text-decoration:none;
  height:49px;line-height:49px;padding:0 20px}
.nav a.is-active{background:linear-gradient(#3a9fdc,#1279bf);padding:0 20px;width:95px;text-align:center}
.nav a.first{padding-left:0}

/* hero */
.hero{left:167px;top:138px;width:772px;height:303px;
  background:linear-gradient(180deg,#cfd9e1 0%,#8aa3b8 20%,#3d8fd0 26%,#6bb7ea 50%,#a7d6f3 75%,#6aa6de 100%)}
.hero-caption{left:167px;top:254px;width:343px;height:102px;background:rgba(14,80,170,.82)}
.hero-caption p{font-family:'Raleway',sans-serif;font-size:24px;line-height:30px;color:var(--white);padding:16px 0 0 30px}
.hero-wave{left:167px;top:338px}
.dots{left:528px;top:416px;display:flex;gap:4px}
.dots span{width:12px;height:12px;border-radius:50%;background:var(--white)}

/* service cards */
.card-img{top:461px;width:257px;height:106px;border-radius:3px}
.card-img.res{left:167px;background:linear-gradient(110deg,#5b6a52,#8a7e6c 45%,#3a86c4 70%,#2c6fb5)}
.card-img.com{left:446px;background:linear-gradient(110deg,#a9cde8,#d6e9f6 50%,#9fc6e6)}
.card-title{top:577px;font-family:'Raleway',sans-serif;font-size:18px;color:var(--navy)}
.card-text{top:601px;width:260px;font-size:8.8px;line-height:14.5px;color:var(--muted)}

/* intro */
.intro-head{left:167px;top:688px;font-family:'Raleway',sans-serif;font-size:21px;color:var(--ink)}
.intro-sub{left:167px;top:719px;font-family:'Raleway',sans-serif;font-size:13px;color:var(--ink)}
.intro-text{left:167px;top:751px;width:545px;font-size:9.2px;line-height:14.5px;color:#333}
.intro-text p+p{margin-top:6px}

/* services */
.svc-head{left:167px;top:853px;font-family:'Raleway',sans-serif;font-size:19.5px;color:var(--navy)}
.svc-text{left:169px;top:881px;width:540px;font-size:9.2px;line-height:14.5px;color:#333}
.check{display:flex;align-items:center;gap:6px;font-size:11.3px;color:#333}
.check i{display:block;width:14px;height:14px}
.bullet{left:172px;font-size:9.6px;color:#333;display:flex;align-items:center;gap:7px}
.bullet:before{content:"";border-left:4px solid #aaa;border-top:3px solid transparent;border-bottom:3px solid transparent}
.btn{left:170px;top:1042px;width:82px;height:24px;border-radius:3px;background:linear-gradient(#2a84d0,#0a5cab);
  color:var(--white);font-size:9.5px;line-height:24px;text-align:center;box-shadow:0 1px 2px rgba(0,0,0,.3)}

/* areas */
.areas{left:728px;top:462px;width:211px;height:426px;border:1px solid #d0d0d0;border-radius:4px;
  background:linear-gradient(#fff 60%,#e6e6e6)}
.areas-head{left:728px;top:462px}
.areas-title{left:728px;top:474px;width:211px;text-align:center;font-family:'Raleway',sans-serif;font-size:17px;color:var(--white)}
.areas-list{left:751px;top:521px;list-style:none}
.areas-list li{height:21.75px;font-size:10.3px;color:#555;display:flex;align-items:center}
.areas-list li:before{content:"";border-left:4px solid var(--navy);border-top:4px solid transparent;border-bottom:4px solid transparent;margin-right:8px}
.areas-list .name{width:96px}

/* testimonial */
.testi{left:729px;top:897px;width:210px;height:170px;border:1px solid #d0d0d0;border-radius:3px;box-shadow:0 1px 3px rgba(0,0,0,.15);text-align:center}
.testi h3{font-family:'Raleway',sans-serif;font-weight:500;font-size:18px;color:var(--ink);margin-top:31px}
.testi blockquote{font-style:italic;font-size:9.8px;line-height:16.8px;color:#555;padding:6px 14px 0}
.testi .author{font-size:9.8px;font-weight:600;color:var(--ocean);margin-top:9px}

/* footer */
.footer{left:0;top:1105px;width:1106px;height:95px;background:linear-gradient(#0a78cf,#1167be)}
.footer-links{left:167px;top:1128px;font-family:'Raleway',sans-serif;font-size:12.2px;color:var(--white);word-spacing:2px}
.footer-copy{left:167px;top:1152px;font-size:8.8px;color:var(--white)}
.social{left:861px;top:1130px;display:flex;gap:12px}
.social span{width:18px;height:18px;border-radius:50%;background:var(--white)}
</style>
</head>
<body>

<header>
  <div class="abs brand"><span class="brand-dot"></span><span class="brand-name">Glimmerwave Pool Service</span></div>
  <div class="abs contact">
    <div class="contact-phone">
      <svg width="18" height="18" viewBox="0 0 18 18"><circle cx="9" cy="9" r="8" fill="none" stroke="#666" stroke-width="1.6"/><path d="M6 5.2c.6-.4 1.1 0 1.4.6l.5 1.1c.2.4 0 .8-.3 1l-.4.3c.4.9 1.1 1.7 2 2.1l.3-.4c.3-.3.7-.4 1.1-.2l1 .6c.5.3.7.9.3 1.3-.6.7-1.4 1-2.2.6C7.6 11.3 6.3 10 5.5 8.1c-.3-.9-.1-2.3.5-2.9z" fill="#666"/></svg>
      858-555-0147
    </div>
    <div class="contact-mail">
      <svg width="13" height="10" viewBox="0 0 13 10"><rect width="13" height="10" rx="1" fill="#777"/><path d="M0.5 1l6 4.5 6-4.5" fill="none" stroke="#fff" stroke-width="1"/></svg>
      info@glimmerwavepool.example
    </div>
  </div>
</header>

<nav class="abs nav">
  <a class="is-active" href="#">Home</a>
  <a href="#">About us</a>
  <a href="#">Services offered</a>
  <a href="#">FAQ's</a>
  <a href="#">Why Hire us</a>
  <a href="#">Contact</a>
</nav>

<section>
  <div class="abs hero" role="img" aria-label="Photo of a sparkling blue swimming pool with a steel ladder and tiled edge"></div>
  <div class="abs hero-caption"><p>Water so pure, it sparkles<br>like a summer sky.</p></div>
  <svg class="abs hero-wave" width="343" height="22" viewBox="0 0 343 22"><path d="M0 14 C90 0 200 2 343 10 L343 16 C200 8 90 6 0 20Z" fill="#33a6d7"/></svg>
  <div class="abs dots"><span></span><span></span><span></span><span></span></div>
</section>

<section>
  <div class="abs card-img res" role="img" aria-label="Photo of a smiling pool technician beside a residential pool with rock waterfall"></div>
  <div class="abs card-img com" role="img" aria-label="Photo of a worker cleaning the tiled floor of an empty commercial pool"></div>
  <h2 class="abs card-title" style="left:169px;font-weight:400">Residential Service</h2>
  <h2 class="abs card-title" style="left:448px;font-weight:400">Commercial Service</h2>
  <p class="abs card-text" style="left:171px">Mauris vel lacus vitae felis vestibulum volutpat Etiam est nunc venenatis in tristique eu imperdiet ac nisl Cum sociis natoque penatibus et magnis dis parturient montes</p>
  <p class="abs card-text" style="left:450px">Mauris vel lacus vitae felis vestibulum volutpat Etiam est nunc venenatis in tristique eu imperdiet ac nisl Cum sociis natoque penatibus et magnis dis parturient montes</p>
</section>

<section>
  <h1 class="abs intro-head" style="font-weight:400">Glimmerwave Pool Service is a leading San Diego</h1>
  <p class="abs intro-sub">swimming pool &amp; spa service company for both residential pools and commercial pools.</p>
  <div class="abs intro-text">
    <p>If you're looking for the BEST pool cleaning service at an affordable price available in San Diego, we would love the opportunity to prove that Glimmerwave Pool Service is the answer. We are a family- owned company that was built on integrity and a commitment to earn and keep each customer's trust with every service and repair.</p>
    <p>Customer satisfaction is our highest priority, and we are proud to see how many of our wonderful customers leave reviews</p>
  </div>
</section>

<section>
  <h2 class="abs svc-head" style="font-weight:400">Services Offered</h2>
  <p class="abs svc-text">Glimmerwave Pool Service is a full service company. We cover the complete spectrum of service and repair. From start-ups to restoring swampy pools, repairing or replacing equipment, Glimmerwave does it all.</p>
  <div class="abs check" style="left:168px;top:925px"><i><svg width="14" height="14" viewBox="0 0 14 14"><circle cx="7" cy="7" r="7" fill="#1a7fd0"/><path d="M3.6 7.2l2.3 2.2 4.4-4.6" fill="none" stroke="#fff" stroke-width="1.8"/></svg></i>Swimming Pool and Spa Cleaning</div>
  <div class="abs check" style="left:382px;top:925px"><i><svg width="14" height="14" viewBox="0 0 14 14"><circle cx="7" cy="7" r="7" fill="#1a7fd0"/><path d="M3.6 7.2l2.3 2.2 4.4-4.6" fill="none" stroke="#fff" stroke-width="1.8"/></svg></i>Install and repair lighting</div>
  <div class="abs check" style="left:168px;top:949px"><i><svg width="14" height="14" viewBox="0 0 14 14"><circle cx="7" cy="7" r="7" fill="#1a7fd0"/><path d="M3.6 7.2l2.3 2.2 4.4-4.6" fill="none" stroke="#fff" stroke-width="1.8"/></svg></i>New Pool and Spa Start Ups</div>
  <div class="abs bullet" style="top:976px">Leak Detection Salt System Conversions</div>
  <div class="abs bullet" style="top:997px">Troubleshoot and Repair pumps, filters, heaters and heat exchangers</div>
  <div class="abs bullet" style="top:1018px">Fountain Cleaning and Service</div>
  <div class="abs btn">READ MORE</div>
</section>

<aside>
  <div class="abs areas"></div>
  <svg class="abs areas-head" width="211" height="46" viewBox="0 0 211 46"><defs><linearGradient id="areasBand" x1="0" y1="0" x2="0" y2="1"><stop offset="0" stop-color="#4ab0e6"/><stop offset="1" stop-color="#0a6fc3"/></linearGradient></defs><path d="M0 4 Q0 0 4 0 H207 Q211 0 211 4 V40 Q105 52 0 40Z" fill="url(#areasBand)"/></svg>
  <h3 class="abs areas-title" style="font-weight:400">Areas Covered</h3>
  <ul class="abs areas-list">
    <li><span class="name">Carmel Valley</span>(92130)</li>
    <li><span class="name">Del Mar</span>(92014)</li>
    <li><span class="name">Rancho Santa Fe</span>(92067)</li>
    <li><span class="name">Solana Beach</span>(92075)</li>
    <li><span class="name">Santaluz</span>(92127)</li>
    <li><span class="name">Cardiff</span>(92007)</li>
    <li><span class="name">Encinitas</span>(92024)</li>
    <li><span class="name">Carlsbad</span>(92009, 92008)</li>
    <li><span class="name">La Jolla</span>(92037)</li>
    <li><span class="name">Pacific Beach</span>(92109)</li>
    <li><span class="name">Mira Mesa</span>(92126)</li>
    <li><span class="name">Sorrento Valley</span>(92121)</li>
    <li><span class="name">Clairemont</span>(92117)</li>
    <li><span class="name">Rancho Bernardo</span>(92127, 92128)</li>
    <li><span class="name">Rancho Penasquitos</span>(92129)</li>
    <li><span class="name">Poway</span>(92064)</li>
  </ul>
  <div class="abs testi">
    <h3>Testimonials</h3>
    <blockquote>&ldquo; Mauris vel lacus vitae felis vestibulum volutpat Etiam est nunc venenatis in tristique eu imperdiet ac nisl Cum sociis natoque penatibus et &rdquo;</blockquote>
    <p class="author">By Author Name, City</p>
  </div>
</aside>

<footer>
  <div class="abs footer"></div>
  <p class="abs footer-links">Home &nbsp;|&nbsp; About us &nbsp;|&nbsp; Services offered &nbsp;|&nbsp; FAQ's &nbsp;|&nbsp; Why Hire us &nbsp;|&nbsp; Contact</p>
  <p class="abs footer-copy">© 2015 Company Name &nbsp;All right reserved &nbsp;Term of Use</p>
  <div class="abs social"><span></span><span></span><span></span></div>
</footer>

</body>
</html>
```